deceased estate clean ups brochures

we would like a brochure to reresent our business we already have new web site and want to do DL A4 brochure to give out to promote our business we already have logo www.brightvale.com.au is where you can get all info needed

Target Market(s)

families with loved ones that have past away
people done sizing or needing to decluter

Colors
cadf82
33b8a4
886aae
33a6d7

```html
<!DOCTYPE html>
<html lang="en">
<head>
<meta charset="utf-8">
<title>Brightvale – Deceased Estate Cleanups Brochure</title>
<link href="https://fonts.googleapis.com/css2?family=Montserrat:wght@400;600;700;800&family=Open+Sans:wght@400;600;700&display=swap" rel="stylesheet">
<style>
:root{
  --green:#6aab3c;
  --green-light:#8dc63f;
  --green-dark:#4f8f2a;
  --charcoal:#333333;
  --charcoal-deep:#2a2a2a;
  --navy:#201f2f;
  --paper:#ffffff;
  --ink:#3a3a3a;
  --bg:#e9e9e9;
}
*{box-sizing:border-box;margin:0;padding:0}
html,body{width:941px;height:1200px;overflow:hidden}
body{background:var(--bg);font-family:"Open Sans",sans-serif;color:var(--ink);position:relative}
.spread{position:absolute;left:70px;width:800px;height:566px;display:flex;box-shadow:0 6px 18px rgba(0,0,0,.18);background:var(--paper)}
.spread--outside{top:22px}
.spread--inside{top:612px}
.panel{position:relative;width:266.67px;height:100%;overflow:hidden}
h2,h3,.brand,.pill,.call-number{font-family:"Montserrat",sans-serif}
.brand{display:flex;align-items:center;gap:7px;font-weight:700;letter-spacing:2px;font-size:20px}
.brand-dot{width:14px;height:14px;border-radius:50%;background:var(--green)}
.photo{position:absolute}
p{font-size:8.5px;line-height:1.45}

/* outside – about */
.about{background:#fafafa}
.about-text{position:absolute;top:34px;left:24px;right:22px}
.about h2{color:var(--green);font-size:17px;font-weight:800;text-transform:uppercase;margin-bottom:12px}
.about p{margin-bottom:8px;text-align:justify}
.about .photo{left:0;right:0;bottom:0;height:270px;background:linear-gradient(160deg,#eef2ec 0%,#d9ddd6 40%,#c9b8a2 75%,#9c8a74 100%)}

/* outside – contact */
.contact{background:var(--charcoal);color:#fff;text-align:center}
.contact .photo{left:0;right:0;top:0;height:150px;background:linear-gradient(180deg,#4a4a4a,#333)}
.contact .brand{position:absolute;top:68px;left:0;right:0;justify-content:center;color:#fff}
.contact h3{position:absolute;top:120px;left:20px;right:20px;font-size:13px;font-weight:800;text-transform:uppercase;line-height:1.25}
.contact-list{position:absolute;top:178px;left:38px;list-style:none;text-align:left}
.contact-list li{display:flex;align-items:center;gap:8px;font-size:9.5px;margin-bottom:14px}
.contact-list svg{width:12px;height:12px;fill:var(--green-light)}
.call-box{position:absolute;top:290px;left:22px;right:22px;border:1.5px solid var(--green-light);padding:26px 8px 14px}
.call-icon{position:absolute;top:-16px;left:50%;margin-left:-16px;width:32px;height:32px;border-radius:50%;background:var(--charcoal);border:1.5px solid var(--green-light);display:flex;align-items:center;justify-content:center}
.call-icon svg{width:14px;height:14px;fill:var(--green-light)}
.call-label{font-family:"Montserrat",sans-serif;font-size:9.5px;font-weight:700;text-transform:uppercase}
.call-number{font-size:26px;font-weight:800;letter-spacing:1px}
.pill{position:absolute;left:34px;right:34px;height:24px;border-radius:12px;font-size:9.5px;font-weight:600;display:flex;align-items:center;justify-content:center}
.contact .pill{top:400px;background:var(--green);color:#fff}

/* outside – cover */
.cover{background:var(--paper)}
.cover .brand{position:absolute;top:30px;left:0;right:0;justify-content:center;color:var(--charcoal);font-size:24px}
.cover .photo{left:20px;right:10px;top:80px;height:230px;background:radial-gradient(ellipse at 50% 45%,#e6e6e6 0%,#cfd4cb 55%,#f4f4f4 100%);border-radius:4px}
.cover-band{position:absolute;left:0;right:0;bottom:0;height:250px}
.cover-title{position:absolute;bottom:96px;left:0;right:0;text-align:center;color:#fff}
.cover-title small{display:block;font-family:"Montserrat",sans-serif;font-size:13px;font-weight:600;text-transform:uppercase}
.cover-title h2{font-size:24px;font-weight:800;text-transform:uppercase;line-height:1.05}
.cover .pill{bottom:52px;background:var(--charcoal-deep);color:#fff}

/* inside – why */
.why{background:var(--paper)}
.why-title{position:absolute;top:26px;left:30px;font-size:13px;font-weight:800;text-transform:uppercase;color:var(--charcoal)}
.why-title::after{content:"";display:inline-block;width:60px;height:1px;background:var(--charcoal);margin-left:8px;vertical-align:middle}
.why-list{position:absolute;top:56px;left:16px;right:18px;list-style:none}
.why-item{position:relative;padding-left:46px;margin-bottom:10px}
.hex{position:absolute;left:4px;top:0;width:24px;height:24px}
.why-item h3{font-size:10px;font-weight:700;color:var(--green);text-transform:uppercase;margin-bottom:2px}
.why-item p{font-size:8px}
.services{position:absolute;left:0;right:0;bottom:0;height:150px;background:var(--navy);color:#fff;padding:20px 16px}
.services-title{font-size:13px;font-weight:800;text-transform:uppercase;color:#fff;margin-bottom:16px}
.services-title::after{content:"";display:inline-block;width:60px;height:1px;background:#fff;margin-left:8px;vertical-align:middle}
.services ul{list-style:none;display:flex;justify-content:space-between}
.services li{width:33%;text-align:center;font-family:"Montserrat",sans-serif;font-size:7.5px;text-transform:uppercase;line-height:1.3;border-right:1px solid rgba(255,255,255,.25);padding:0 4px}
.services li:last-child{border-right:0}
.services svg{width:28px;height:28px;fill:var(--green-light);display:block;margin:0 auto 6px}

/* inside – steps */
.steps{background:var(--green);color:#fff;padding:26px 24px}
.steps-title{font-size:13px;font-weight:800;text-transform:uppercase;margin-bottom:14px}
.steps-title::after{content:"";display:inline-block;width:50px;height:1px;background:#fff;margin-left:8px;vertical-align:middle}
.step-list{list-style:none;border-left:1.5px solid rgba(255,255,255,.7);margin-left:5px}
.step{position:relative;padding-left:16px;margin-bottom:11px}
.step::before{content:"";position:absolute;left:-6px;top:1px;width:9px;height:9px;border-radius:50%;border:1.5px solid #fff;background:var(--green)}
.step h3{font-size:9px;font-weight:700;text-transform:uppercase;margin-bottom:2px}
.step p{font-size:8px}
.ticks{list-style:none}
.ticks li{font-size:8px;line-height:1.4;padding-left:11px;position:relative}
.ticks li::before{content:"✓";position:absolute;left:0;font-weight:700}

/* inside – testimonials */
.reviews{background:var(--paper)}
.reviews svg.curve{position:absolute;left:0;top:0}
.reviews .brand{position:absolute;top:40px;right:14px;color:var(--charcoal);font-size:17px;letter-spacing:1.5px}
.quote{position:absolute;right:16px}
.quote p{font-size:8.5px;text-align:justify}
.quote p::before{content:"\201C";font-family:Georgia,serif;font-size:26px;color:var(--green);line-height:0;vertical-align:-10px;margin-right:3px}
.quote cite{display:block;text-align:right;font-style:normal;font-family:"Montserrat",sans-serif;font-size:8.5px;font-weight:700;margin-top:4px;color:var(--charcoal)}
.quote cite span{color:var(--green)}
.quote--first{top:96px;left:114px}
.quote--second{top:250px;left:86px}
.quote--third{top:385px;left:68px}
</style>
</head>
<body>

<section class="spread spread--outside" aria-label="Brochure outside">
  <article class="panel about">
    <div class="about-text">
      <h2>About Our Company</h2>
      <p>At Brightvale our goal is to ease your worries and help you with your journey in preparing your house for rental or resale.</p>
      <p>Whether it is a move to another residence or the difficult task of dealing with the grief when a loved one passes away, Brightvale can help with the preparation of the property for sale.</p>
      <p>Brightvale will come in, remove unwanted items and dispose of all rubbish, do cosmetic repairs if required and leave the property in a spotless state.</p>
    </div>
    <div class="photo" role="img" aria-label="Photo of a consultant shaking hands with an older couple at a table"></div>
  </article>

  <article class="panel contact">
    <div class="photo" role="img" aria-label="Faded photo of cleaners at work"></div>
    <div class="brand"><span class="brand-dot"></span>BRIGHTVALE</div>
    <h3>If you have any queries,<br>get in touch with us.</h3>
    <ul class="contact-list">
      <li><svg viewBox="0 0 24 24"><path d="M6.6 10.8a15 15 0 006.6 6.6l2.2-2.2a1 1 0 011-.25 11.4 11.4 0 003.6.57 1 1 0 011 1V20a1 1 0 01-1 1A17 17 0 013 4a1 1 0 011-1h3.5a1 1 0 011 1c0 1.25.2 2.45.57 3.6a1 1 0 01-.25 1z"/></svg>0400 123 456</li>
      <li><svg viewBox="0 0 24 24"><path d="M2 5h20v14H2zm2 2v.5l8 5 8-5V7z"/></svg>info@brightvale.com.au</li>
      <li><svg viewBox="0 0 24 24"><path d="M12 2a7 7 0 00-7 7c0 5 7 13 7 13s7-8 7-13a7 7 0 00-7-7zm0 9.5A2.5 2.5 0 1112 6.5a2.5 2.5 0 010 5z"/></svg>PO Box 210, Northgate 3099</li>
    </ul>
    <div class="call-box">
      <div class="call-icon"><svg viewBox="0 0 24 24"><path d="M6.6 10.8a15 15 0 006.6 6.6l2.2-2.2a1 1 0 011-.25 11.4 11.4 0 003.6.57 1 1 0 011 1V20a1 1 0 01-1 1A17 17 0 013 4a1 1 0 011-1h3.5a1 1 0 011 1c0 1.25.2 2.45.57 3.6a1 1 0 01-.25 1z"/></svg></div>
      <div class="call-label">Call us for more details</div>
      <div class="call-number">0400 123 456</div>
    </div>
    <div class="pill">www.brightvale.com.au</div>
  </article>

  <article class="panel cover">
    <div class="brand"><span class="brand-dot"></span>BRIGHTVALE</div>
    <div class="photo" role="img" aria-label="Photo of two cleaners in aprons and yellow gloves holding cleaning spray"></div>
    <svg class="cover-band" viewBox="0 0 267 250" preserveAspectRatio="none" aria-hidden="true">
      <path d="M0 90 Q140 20 267 0 V250 H0Z" fill="#333"/>
      <path d="M0 100 Q140 32 267 14 V250 H0Z" fill="#6aab3c"/>
    </svg>
    <div class="cover-title"><small>We are to help</small><h2>Deceased Estate<br>Cleanups</h2></div>
    <div class="pill">www.brightvale.com.au</div>
  </article>
</section>

<section class="spread spread--inside" aria-label="Brochure inside">
  <article class="panel why">
    <h2 class="why-title">Why Choose Us</h2>
    <ul class="why-list">
      <li class="why-item"><svg class="hex" viewBox="0 0 24 24"><polygon points="12,1 22,6.5 22,17.5 12,23 2,17.5 2,6.5" fill="#8dc63f"/></svg><h3>Quality</h3><p>Our goal is to enhance your property and achieve the results you are looking for. We appreciate the trust placed in us to deliver a quality job that meets your expectations.</p></li>
      <li class="why-item"><svg class="hex" viewBox="0 0 24 24"><polygon points="12,1 22,6.5 22,17.5 12,23 2,17.5 2,6.5" fill="#8dc63f"/></svg><h3>Professionalism</h3><p>Brightvale only uses quality staff and materials that are fit for purpose. We keep a professional approach to every job, ensuring all agreed tasks are completed and accounted.</p></li>
      <li class="why-item"><svg class="hex" viewBox="0 0 24 24"><polygon points="12,1 22,6.5 22,17.5 12,23 2,17.5 2,6.5" fill="#8dc63f"/></svg><h3>Pride</h3><p>We take pride in our family approach and care we bring to your loved ones' belongings. Whether it is simple house clearing, house repairs or larger renovations.</p></li>
      <li class="why-item"><svg class="hex" viewBox="0 0 24 24"><polygon points="12,1 22,6.5 22,17.5 12,23 2,17.5 2,6.5" fill="#8dc63f"/></svg><h3>Areas Serviced</h3><p>Specialising in Melbourne CBD and suburbs including: Coburg, Fawkner, Campbellfield, Craigieburn, St. Kilda, Brighton, Caulfield, Hawthorn, Heidelberg, Watsonia...</p></li>
    </ul>
    <div class="services">
      <h2 class="services-title">Services Offered</h2>
      <ul>
        <li><svg viewBox="0 0 24 24"><path d="M12 3l10 9h-3v9H5v-9H2z"/></svg>Cleaning<br>Service</li>
        <li><svg viewBox="0 0 24 24"><path d="M9 2h6v3h-2v2h3l2 3v12H6V10l2-3h1zm-1 11v6h8v-6z"/></svg>Preparation for<br>rental or sale</li>
        <li><svg viewBox="0 0 24 24"><path d="M19 2l2 2-8 8 1 1-3 3-5-5 3-3 1 1zM4 14l6 6-4 2-4-4z"/></svg>Garden<br>Makeovers</li>
      </ul>
    </div>
  </article>

  <article class="panel steps">
    <h2 class="steps-title">Our 5 Step Process</h2>
    <ol class="step-list">
      <li class="step"><h3>Step 1:</h3><p>We start with a consultation at the property, understanding our client's needs, requests and priorities. Create a plan of what needs to be done in each step of your move. Provide a personalized quote.</p></li>
      <li class="step"><h3>Step 2:</h3><p>Pre-sale decluttering and sorting of items. Unwanted items to be sold, given to friends, family or charity.</p></li>
      <li class="step"><h3>Step 3:</h3>
        <ul class="ticks">
          <li>We thoroughly clear and clean the property (inside and outside) prior to sale or rent.</li>
          <li>House to be staged and set up to enhance its presentation for sale or rent.</li>
          <li>Rubbish to be picked up.</li>
          <li>Garden to be tidied.</li>
          <li>After settlement, we begin to pack your possessions, ready to be moved as directed.</li>
        </ul></li>
      <li class="step"><h3>Step 4:</h3><p>Organising and arranging transport of your possessions.</p></li>
      <li class="step"><h3>Step 5:</h3><p>Storage or unpacking your possessions and setting up as per your instructions.</p></li>
    </ol>
  </article>

  <article class="panel reviews">
    <svg class="curve" width="267" height="566" viewBox="0 0 267 566" aria-hidden="true">
      <path d="M0 0 H120 Q60 150 45 300 Q35 430 30 566 H0Z" fill="#6aab3c"/>
      <path d="M120 0 Q60 150 45 300 Q35 430 30 566 H44 Q49 430 59 300 Q74 150 134 0Z" fill="#333"/>
      <path d="M134 0 Q74 150 59 300 Q49 430 44 566 H52 Q57 430 67 300 Q82 150 142 0Z" fill="#8dc63f"/>
    </svg>
    <div class="brand"><span class="brand-dot"></span>BRIGHTVALE</div>
    <blockquote class="quote quote--first"><p>The Brightvale crew did a fantastic job in cleaning out my parent's house in preparation for an estate auction. The communication was outstanding and his knowledge of what could make for a good auction item was very valuable.</p><cite><span>-DANIEL,</span> CUSTOMER</cite></blockquote>
    <blockquote class="quote quote--second"><p>Brightvale provides estate clean out services for both commercial and residential clients. They got rid of unwanted items and junk. They promise affordable prices for their services and that's exactly what we received.</p><cite><span>-OLIVER,</span> CUSTOMER</cite></blockquote>
    <blockquote class="quote quote--third"><p>Check out Brightvale if you are in need of home, building, and storage units clean out services that will suit your needs. They also handle estate sales and are always available on time.</p><cite><span>-THOMAS,</span> CUSTOMER</cite></blockquote>
  </article>
</section>

</body>
</html>
```